Visitenkarte erstellen für Reiki Praxis

Visitenkarten für Reiki Praxis Doppelseitig

business cards reiki practice double-sided

The background can also be a different color

```html
<!DOCTYPE html>
<html lang="en">
<head>
<meta charset="utf-8">
<title>Still River Reiki – Business Cards</title>
<link rel="stylesheet" href="https://fonts.googleapis.com/css2?family=Lato:wght@400;700&family=Montserrat:wght@400&display=swap">
<style>
  :root {
    --page: #ececec;
    --card: #0e0e0e;
    --card-tone: #161616;
    --gold: #e0a526;
    --white: #ffffff;
    --text: #f1f1f1;
    --rose: #b9718f;
    --peach: #e9b07c;
  }
  * { margin: 0; padding: 0; box-sizing: border-box; }
  html, body {
    width: 1200px; height: 1200px; overflow: hidden;
    background: var(--page);
  }
  .sheet { position: relative; width: 1200px; height: 1200px; }

  .card {
    position: absolute;
    border-radius: 19px;
    overflow: hidden;
    background: var(--card);
  }
  .card--front { left: 188px; top: 91px; width: 823px; height: 474px; }
  .card--back  { left: 186px; top: 635px; width: 829px; height: 473px; }

  .card__pattern {
    position: absolute; inset: 0;
    background: radial-gradient(ellipse at 50% 50%, var(--card-tone) 0%, var(--card) 80%);
  }

  .brand { position: absolute; text-align: center; }
  .brand__mark {
    display: block; margin: 0 auto;
    border-radius: 50%;
    border: 1.5px solid var(--peach);
  }
  .brand__name {
    display: block;
    font-family: 'Lato', sans-serif;
    font-weight: 400;
    color: var(--white);
    white-space: nowrap;
    letter-spacing: 0.01em;
  }
  .brand__person {
    display: block;
    font-family: 'Montserrat', sans-serif;
    font-weight: 400;
    color: var(--gold);
    white-space: nowrap;
  }

  .card--front .brand { left: 36px; width: 360px; top: 165px; }
  .card--front .brand__mark { width: 66px; height: 66px; margin-top: 8px; }
  .card--front .brand__name { font-size: 33px; line-height: 1; margin-top: 20px; }
  .card--front .brand__person { font-size: 22px; letter-spacing: 0.26em; line-height: 1; margin-top: 5px; padding-left: 0.26em; }

  .divider {
    position: absolute; left: 412px; top: 131px;
    width: 2px; height: 213px;
    background: linear-gradient(to bottom, var(--gold), var(--rose));
  }

  .contact { position: absolute; left: 449px; top: 129px; font-family: 'Lato', sans-serif; color: var(--text); }
  .contact__name { font-size: 27px; font-weight: 700; color: var(--gold); line-height: 1; letter-spacing: 0.01em; }
  .contact__role { font-size: 20px; line-height: 1; margin-top: 9px; }
  .contact__list { list-style: none; margin-top: 21px; }
  .contact__item { position: relative; padding-left: 26px; font-size: 20px; line-height: 29px; }
  .contact__item--address { margin-bottom: 10px; }
  .contact__icon {
    position: absolute; left: 0; top: 5px;
    width: 19px; height: 19px;
    fill: none; stroke: var(--gold); stroke-width: 1.6;
  }

  .card--back .brand { left: 0; width: 829px; top: 126px; }
  .card--back .brand__mark { width: 110px; height: 110px; margin-top: 14px; }
  .card--back .brand__name { font-size: 52px; line-height: 1; margin-top: 32px; }
  .card--back .brand__person { font-size: 34px; letter-spacing: 0.3em; line-height: 1; margin-top: 10px; padding-left: 0.3em; }
</style>
</head>
<body>
<main class="sheet">

  <section class="card card--front">
    <div class="card__pattern" role="img" aria-label="Faint repeating floral pattern across the card background"></div>

    <div class="brand">
      <span class="brand__mark"></span>
      <span class="brand__name">STILL RIVER REIKI</span>
      <span class="brand__person">MARA VEIT</span>
    </div>

    <div class="divider"></div>

    <div class="contact">
      <p class="contact__name">DANIEL BROOKS</p>
      <p class="contact__role">General Manager</p>
      <ul class="contact__list">
        <li class="contact__item contact__item--address">
          <svg class="contact__icon" viewBox="0 0 20 20"><path d="M10 18.5s-6-6.2-6-10.5a6 6 0 0 1 12 0c0 4.3-6 10.5-6 10.5z"/><circle cx="10" cy="8" r="2.3"/></svg>
          1400 Maplewood Ave. Suite 220<br>Fairhaven, OR 97321
        </li>
        <li class="contact__item">
          <svg class="contact__icon" viewBox="0 0 20 20"><path d="M5 2.5l3 3.5-1.8 2.2c1 2.2 2.8 4 5 5L13.4 11.4l3.6 3-1.6 2.6C9 17 3 11 3 4.6z"/><path d="M12 3a5 5 0 0 1 5 5M12 6a2 2 0 0 1 2 2"/></svg>
          000-123-456789
        </li>
        <li class="contact__item">
          <svg class="contact__icon" viewBox="0 0 20 20"><rect x="2" y="5" width="16" height="11"/><path d="M2 5l8 6 8-6M2 16l6-5M18 16l-6-5"/></svg>
          info@yourwebsitename.com
        </li>
        <li class="contact__item">
          <svg class="contact__icon" viewBox="0 0 20 20"><circle cx="10" cy="10" r="7.5"/><ellipse cx="10" cy="10" rx="3.3" ry="7.5"/><path d="M2.5 10h15M3.8 6h12.4M3.8 14h12.4"/></svg>
          www.yourwebsitename.com
        </li>
      </ul>
    </div>
  </section>

  <section class="card card--back">
    <div class="card__pattern" role="img" aria-label="Faint repeating floral pattern across the card background"></div>

    <div class="brand">
      <span class="brand__mark"></span>
      <span class="brand__name">STILL RIVER REIKI</span>
      <span class="brand__person">MARA VEIT</span>
    </div>
  </section>

</main>
</body>
</html>
```